Valdmont Construction Services
Building Modern Luxury
Valdmont Construction Services - Construction
Creative Brief
Construction
www.valsorvo.com
We specialize in Custom homes Commercial, Renovations, and metal buildings
We do not want a cluttery website. We want VERY modern with minimal text and Photos. Clean lines and not curves
High Tech
Black background and Black box
Greys, some white
some green
top
http://www.pinelakeestates.com/#home/
http://www.tolmanstudio.com/
We want a black background with a black rectangular box for the template(similar to pinelakeestates.com) We also want a Enter site page that jsut has our logo in the middle with Building Modern Luxury in white font and a Enter Here sign(like on Tolmanstudio.com but without photos) Maybe a dark grey siloette or outline of a house or roofs in the background(barely noticeable) integrated in the site. We want the second page to be the template page..preferbly a rectangular box that has a place for text and a place for a photo. We want our logo on each page. We want a tab for Home, Custom homes, commercial , renovations, metal buildings, and contact. We want the phone # to be on the top right on EVERY page 555 214 0376. We want our template to hold a place for text and a place for ONE photo( this photo box will be a slideshow for more photos) We want copyright info under the bottom of the rectangular template. We have also attached .a url of our logo and business card

```html
<!DOCTYPE html>
<html lang="en">
<head>
<meta charset="utf-8">
<title>Valdmont Construction Services — Building Modern Luxury</title>
<link rel="stylesheet" href="https://fonts.googleapis.com/css2?family=Roboto:wght@400;500;700&display=swap">
<style>
  :root {
    --bg: #000000;
    --panel: #050505;
    --frame: #6f7a52;
    --green: #8cc63f;
    --green-soft: #a6d05a;
    --white: #ffffff;
    --grey-light: #cfcfcf;
    --grey: #9a9a9a;
    --grey-dark: #3a3a3a;
    --grey-deep: #1a1a1a;
    --font: 'Roboto', Arial, sans-serif;
  }
  * { margin: 0; padding: 0; box-sizing: border-box; }
  html, body { width: 1200px; height: 914px; overflow: hidden; background: var(--bg); font-family: var(--font); }
  .page { position: relative; width: 1200px; height: 914px; background: var(--bg); }

  /* header */
  .brand { position: absolute; left: 160px; top: 18px; width: 210px; text-align: center; color: var(--white); }
  .brand-mark { width: 84px; height: 84px; border-radius: 50%; background: #5c5c5c; margin: 0 auto 8px; }
  .brand-name { font-size: 44px; font-weight: 400; letter-spacing: 1px; line-height: 1; }
  .brand-sub { font-size: 11px; font-weight: 400; letter-spacing: 2px; margin-top: 6px; }

  .call { position: absolute; right: 94px; top: 28px; display: flex; align-items: center; gap: 12px; color: var(--green); font-size: 29px; font-weight: 400; }
  .call svg { width: 30px; height: 30px; }
  .social { position: absolute; right: 164px; top: 86px; display: flex; gap: 10px; }
  .social span { width: 28px; height: 28px; background: #4a6fae; border-radius: 3px; }
  .social span + span { background: #5aaee0; }
  .tagline { position: absolute; right: 94px; top: 138px; color: var(--grey-light); font-size: 30px; font-weight: 400; letter-spacing: 1px; }

  /* main box */
  .frame { position: absolute; left: 158px; top: 183px; width: 884px; height: 664px; border: 2px solid var(--frame); border-radius: 6px; background: var(--panel); }

  .nav { position: absolute; left: 0; top: 8px; width: 100%; height: 42px; display: flex; align-items: center; padding-left: 10px; }
  .nav a { color: var(--white); text-decoration: none; font-size: 17px; height: 100%; display: flex; align-items: center; justify-content: center; border-right: 1px solid var(--grey-dark); }
  .nav a:last-child { border-right: none; }
  .nav a.is-active { color: var(--green); }

  .slideshow { position: absolute; left: 6px; top: 62px; width: 870px; height: 420px; overflow: hidden; }
  .slide-photo { position: absolute; inset: 0; background: linear-gradient(180deg, #6a1a0c 0%, #c2411a 20%, #8a2a14 38%, #3a1710 60%, #1a0d0a 80%, #0b0706 100%); }
  .slide-arrow { position: absolute; top: 150px; width: 34px; height: 44px; background: var(--white); border-radius: 4px; display: flex; align-items: center; justify-content: center; }
  .slide-arrow svg { width: 16px; height: 20px; }
  .slide-arrow.prev { left: 0; border-radius: 0 4px 4px 0; }
  .slide-arrow.next { right: 0; border-radius: 4px 0 0 4px; }

  .intro { position: absolute; left: 0; bottom: 0; width: 100%; height: 146px; background: rgba(20, 20, 20, 0.72); padding: 16px 26px; }
  .intro-title { color: var(--green-soft); font-size: 19px; font-weight: 400; margin-bottom: 8px; }
  .intro-text { color: var(--grey-light); font-size: 12.5px; line-height: 1.55; }

  .projects { position: absolute; left: 6px; top: 482px; width: 870px; height: 166px; background: linear-gradient(180deg, #2b2b2b 0%, #141414 100%); }
  .projects-arrow { position: absolute; top: 62px; width: 20px; height: 26px; }
  .projects-arrow.prev { left: 14px; }
  .projects-arrow.next { right: 14px; }
  .project { position: absolute; top: 16px; width: 148px; }
  .project-photo { width: 148px; height: 114px; border: 2px solid var(--grey-light); }
  .project-label { margin-top: 4px; height: 26px; border: 1px solid var(--grey); border-radius: 3px; background: #0c0c0c; color: var(--white); font-size: 14px; display: flex; align-items: center; justify-content: center; }
  .photo-homes { background: linear-gradient(180deg, #7ea3c9 0%, #6b6a60 55%, #3d4a2a 100%); }
  .photo-commercial { background: linear-gradient(180deg, #10162e 0%, #3a2a4a 50%, #c28a3a 100%); }
  .photo-renovations { background: linear-gradient(180deg, #b7cde0 0%, #c9a67a 55%, #8a6a45 100%); }
  .photo-metal { background: linear-gradient(180deg, #e6e6e6 0%, #9a9a9a 55%, #5a5a5a 100%); }

  /* footer */
  .copyright { position: absolute; left: 160px; top: 868px; color: var(--grey-dark); font-size: 11px; }
  .footer-brand { position: absolute; left: 982px; top: 854px; text-align: center; color: var(--white); }
  .footer-brand .mark { width: 24px; height: 24px; border-radius: 50%; background: #5c5c5c; margin: 0 auto 2px; }
  .footer-brand .name { font-size: 11px; letter-spacing: 0.5px; }
</style>
</head>
<body>
<div class="page">

  <header>
    <div class="brand">
      <div class="brand-mark"></div>
      <div class="brand-name">VALDMONT</div>
      <div class="brand-sub">CONSTRUCTION SERVICES</div>
    </div>

    <div class="call">
      <svg viewBox="0 0 30 30" aria-hidden="true">
        <circle cx="15" cy="15" r="15" fill="#8cc63f"/>
        <path d="M10 8 h4 l1 4 -2 1.5 c1 2.5 2.5 4 5 5 l1.5 -2 4 1 v4 c-8 1 -14 -5 -13.5 -13.5z" fill="#000"/>
      </svg>
      <span>CALL NOW: <span>555 214 0376</span></span>
    </div>

    <div class="social" aria-hidden="true"><span></span><span></span></div>

    <div class="tagline">BUILDING MODERN LUXURY</div>
  </header>

  <main class="frame">
    <nav class="nav">
      <a href="#" class="is-active" style="width:106px">Home</a>
      <a href="#" style="width:150px">Custom Homes</a>
      <a href="#" style="width:154px">Commercial</a>
      <a href="#" style="width:150px">Renovations</a>
      <a href="#" style="width:170px">Metal Buildings</a>
      <a href="#" style="width:134px">Contact Us</a>
    </nav>

    <section class="slideshow">
      <div class="slide-photo" role="img" aria-label="Aerial view of a dense city skyline under a glowing orange sunset sky"></div>
      <div class="slide-arrow prev"><svg viewBox="0 0 16 20"><path d="M12 2 L3 10 L12 18" fill="none" stroke="#111" stroke-width="3"/></svg></div>
      <div class="slide-arrow next"><svg viewBox="0 0 16 20"><path d="M4 2 L13 10 L4 18" fill="none" stroke="#111" stroke-width="3"/></svg></div>

      <div class="intro">
        <h1 class="intro-title">WELCOME TO VALDMONT CONSTRUCTION SERVICES</h1>
        <p class="intro-text">We build modern homes and commercial spaces with clean lines, honest materials and careful detail. From the first sketch to the final walkthrough, our team manages every stage of the project with clear schedules and open communication. Whether you are planning a custom residence, renovating an existing property or raising a steel building for your business, we bring the same standard of precision to each site. Our crews work with trusted suppliers and modern methods to deliver structures that look sharp, perform well and last for decades. Contact us to discuss your next project.</p>
      </div>
    </section>

    <section class="projects">
      <svg class="projects-arrow prev" viewBox="0 0 20 26"><path d="M15 3 L5 13 L15 23" fill="none" stroke="#fff" stroke-width="3"/></svg>
      <svg class="projects-arrow next" viewBox="0 0 20 26"><path d="M5 3 L15 13 L5 23" fill="none" stroke="#fff" stroke-width="3"/></svg>

      <div class="project" style="left:52px">
        <div class="project-photo photo-homes" role="img" aria-label="Stone custom home with gabled roof"></div>
        <div class="project-label">Custom Homes</div>
      </div>
      <div class="project" style="left:260px">
        <div class="project-photo photo-commercial" role="img" aria-label="Lit commercial towers at night"></div>
        <div class="project-label">Commercial</div>
      </div>
      <div class="project" style="left:470px">
        <div class="project-photo photo-renovations" role="img" aria-label="Timber house frame under renovation"></div>
        <div class="project-label">Renovations</div>
      </div>
      <div class="project" style="left:678px">
        <div class="project-photo photo-metal" role="img" aria-label="Modern metal-clad building facade"></div>
        <div class="project-label">Metal Buildings</div>
      </div>
    </section>
  </main>

  <footer>
    <p class="copyright">Copyright © 2011 VALDMONT CONSTRUCTION SERVICES. All Rights Reserved.</p>
    <div class="footer-brand">
      <div class="mark"></div>
      <div class="name">VALDMONT</div>
    </div>
  </footer>

</div>
</body>
</html>
```